WEB PAGES DESIGN

We need a web design for a new company called "NEXO47". Our major business is that provide Internet Data Center solution, such as: rack/colocation, bandwidth, dedicated server, cloud server, CDN, and so on.
Requirements of Design:
1. Home page layout can refer to index-content.jpg in the attachments, but not limited.
2. According to match logo colors to design colors of web pages, Logo in the attachments.
3. The web contents of home page in image of the index-content.jpg.
4. The successful bidder will need to design three banner.

```html
<!DOCTYPE html>
<html lang="en">
<head>
<meta charset="utf-8">
<title>NEXO47 — Your Internet Data Solutions</title>
<link rel="stylesheet" href="https://fonts.googleapis.com/css2?family=Exo:wght@400;500;600&family=Ubuntu:wght@500;700&display=swap">
<style>
:root{
  --green:#7dbb2e;
  --green-dark:#5e9a1c;
  --green-text:#6aa924;
  --ink:#333;
  --charcoal:#3b3b3b;
  --panel:#2a2a2c;
  --footer:#434343;
  --card:#e6e6e6;
  --muted:#555;
}
*{box-sizing:border-box;margin:0;padding:0}
html,body{width:1106px;height:1200px;overflow:hidden;background:#fff}
body{position:relative;font-family:Arial,Helvetica,sans-serif;color:var(--ink)}
.abs{position:absolute}
.topline{left:0;top:0;width:1106px;height:5px;background:#3a3a3a}
.brand{display:flex;align-items:center;gap:6px;font-family:"Exo",sans-serif;font-weight:600}
.brand-mark{display:block}
.header-brand{left:183px;top:40px;font-size:18px;color:#3a3a3a}
.header-brand .brand-mark{width:20px;height:20px;background:var(--green)}
.tagline{left:322px;top:42px;font-family:"Exo",sans-serif;font-weight:600;font-size:24px;letter-spacing:-.3px;color:#3a3a3a}
.tagline em{font-style:normal;color:var(--green)}
.inquiry{left:760px;top:33px;width:164px;text-align:right;font-size:10px;color:#333}
.phone{display:flex;align-items:center;gap:5px;font-family:"Exo",sans-serif;font-weight:600}
.header-phone{left:766px;top:45px;font-size:20px;color:#222}
.nav{left:0;top:104px;width:1106px;height:35px;background:linear-gradient(#8fcb3f,#6fae25);border-bottom:3px solid #4f8418}
.nav a{position:absolute;top:0;height:35px;line-height:35px;font-family:"Exo",sans-serif;font-size:12px;letter-spacing:1px;color:#fff;text-decoration:none;text-transform:uppercase;transform:translateX(-50%)}
.nav .sep{position:absolute;top:0;width:1px;height:35px;background:#4f8418;box-shadow:1px 0 0 #a6d962}
.hero{left:0;top:144px;width:1106px;height:272px;background:linear-gradient(90deg,#5e5e5e 0,#868686 22%,#9a9a9a 40%,#6e6e6e 62%,#7c7c7c 85%,#5a5a5a 100%)}
.hero-panel{left:676px;top:144px;width:272px;height:226px}
.hero-title{left:676px;top:164px;width:264px;text-align:center;font-family:"Exo",sans-serif;font-weight:500;font-size:28px;line-height:29px;color:#e8e8e8}
.hero-copy{left:696px;top:228px;width:224px;text-align:center;font-size:11px;line-height:13.5px;color:#cfcfcf}
.btn{left:741px;top:284px;width:147px;height:25px;line-height:23px;text-align:center;background:linear-gradient(#86c73a,#5f9f1e);border:1px solid #a7dc69;font-family:"Exo",sans-serif;font-size:11px;color:#fff;text-decoration:none}
.core{left:0;top:416px;width:1106px;height:338px;background:var(--charcoal)}
.core-box{left:181px;top:432px;width:744px;height:310px;border-radius:8px;border:2px solid #555;background:linear-gradient(160deg,#262626,#0c0c0c 60%,#1c1c1c)}
.core-title{left:181px;top:428px;width:744px;text-align:center;font-family:"Exo",sans-serif;font-weight:400;font-size:24px;color:#f0f0f0}
.core-title strong{color:var(--green);font-weight:600}
.card{width:328px;height:100px;border-radius:8px;background:linear-gradient(165deg,#f0f0f0,#dcdcdc)}
.card-icon{position:absolute;left:20px;top:22px;width:92px;height:56px;border-radius:4px;background:linear-gradient(#8ed043,#4f8d16);box-shadow:0 4px 0 #3d6d12}
.card h3{position:absolute;left:126px;top:20px;font-family:"Ubuntu",sans-serif;font-weight:700;font-size:16px;letter-spacing:.5px;color:var(--green-text);text-transform:uppercase}
.card p{position:absolute;left:126px;top:42px;width:190px;font-size:9.6px;line-height:11.8px;color:#222}
.partners-title{left:0;top:772px;width:1115px;text-align:center;font-family:"Ubuntu",sans-serif;font-weight:700;font-size:9.5px;color:var(--green-text)}
.rule{height:1px;background:linear-gradient(90deg,transparent,#ccc 20%,#ccc 80%,transparent)}
.partner{top:806px;height:22px;border-radius:3px;background:#bdbdbd}
.section-head{font-family:"Ubuntu",sans-serif;font-weight:700;font-size:19px;color:var(--green-text);text-transform:uppercase}
.news-head{left:226px;top:891px;font-family:"Ubuntu",sans-serif;font-weight:500;font-size:11.5px;color:#222}
.body-text{font-size:9.7px;line-height:11.6px;color:#333}
.more{font-size:9.7px;font-weight:bold;color:var(--green-text);text-decoration:none}
.footer{left:0;top:998px;width:1106px;height:173px;background:var(--footer)}
.footer-brand{left:187px;top:1080px;font-size:22px;color:#fff}
.footer-brand .brand-mark{width:22px;height:22px;background:#fff}
.foot-head{font-family:"Ubuntu",sans-serif;font-weight:700;font-size:14px;letter-spacing:.4px;color:#fff;text-transform:uppercase}
.foot-list{list-style:none;font-size:9.6px;line-height:14.2px}
.foot-list a{color:#e4e4e4;text-decoration:none}
.social{left:560px;top:1063px;display:flex;gap:7px}
.social span{width:22px;height:22px;border-radius:50%;background:#fff}
.address{left:775px;top:1062px;font-size:9.6px;line-height:14px;color:#eee}
.email{left:777px;top:1089px;font-size:12px;color:#fff}
.footer-phone{left:775px;top:1106px;font-size:19px;color:#fff;font-weight:400}
.bottom{left:0;top:1171px;width:1106px;height:29px;background:var(--green)}
.copy{left:183px;top:1180px;font-size:8.2px;color:#fff}
.legal{left:700px;top:1180px;width:224px;text-align:right;font-size:8.2px;color:#fff}
.legal a{color:#fff;text-decoration:none}
</style>
</head>
<body>
<div class="abs topline"></div>

<header>
  <div class="abs brand header-brand"><span class="brand-mark"></span>NEXO47</div>
  <div class="abs tagline">YOUR <em>INTERNET DATA</em> SOLUTIONS</div>
  <div class="abs inquiry">For Inquiries Contact us</div>
  <div class="abs phone header-phone">
    <svg width="20" height="20" viewBox="0 0 20 20"><circle cx="10" cy="10" r="9" fill="none" stroke="#222" stroke-width="1.5"/><path d="M7 5.5c-1 .6-1.3 1.8-.8 3.2.9 2.4 2.6 4.3 4.9 5.4 1.3.6 2.5.3 3.1-.6l-1.8-1.7-1.3.8c-1-.5-2-1.6-2.5-2.7l.9-1.2z" fill="#222"/></svg>
    0-10-5550147
  </div>
</header>

<nav class="abs nav">
  <a href="#" style="left:248px">Home</a><span class="sep" style="left:300px"></span>
  <a href="#" style="left:396px">Dedicated Server</a><span class="sep" style="left:495px"></span>
  <a href="#" style="left:553px">Hosting</a><span class="sep" style="left:614px"></span>
  <a href="#" style="left:695px">Data Centers</a><span class="sep" style="left:779px"></span>
  <a href="#" style="left:843px">About Us</a>
</nav>

<section>
  <div class="abs hero" role="img" aria-label="Banner artwork: green globe beside server racks over a grey digital number backdrop"></div>
  <svg class="abs hero-panel" viewBox="0 0 272 226"><polygon points="0,0 272,0 272,160 136,225 0,160" fill="var(--panel)" opacity=".96"/></svg>
  <h1 class="abs hero-title">IDC<br>SOLUTIONS</h1>
  <p class="abs hero-copy">NEXO47 provides a wide range of highly specialized solutions that utilizes technology to transform your organization.</p>
  <a class="abs btn" href="#">read more</a>
</section>

<section class="abs core"></section>
<div class="abs core-box"></div>
<svg class="abs" style="left:183px;top:434px" width="740" height="70" viewBox="0 0 740 70"><path d="M0 0H740V10C600 60 460 60 370 50C250 40 120 20 0 20Z" fill="#3a3a3a"/></svg>
<h2 class="abs core-title">Get <strong>NEXO47</strong> Core Technologies</h2>

<div class="abs card" style="left:207px;top:504px">
  <div class="card-icon" role="img" aria-label="Green block icon with a server tower"></div>
  <h3>Dedicated Servers</h3>
  <p>Consectetur adipisicing elit, sed do eiusmod tempor incididunt ut labore et dolore magna aliqua. Ut enim ad minim veniam.</p>
</div>
<div class="abs card" style="left:565px;top:504px">
  <div class="card-icon" role="img" aria-label="Green block icon with a hard drive"></div>
  <h3>Hosting Servers</h3>
  <p>Sed ut perspiciatis, unde omnis ise natus error sit voluptatem accusantium doloremque laudantium, totam rem.</p>
</div>
<div class="abs card" style="left:207px;top:620px">
  <div class="card-icon" role="img" aria-label="Green block icon with stacked rack units"></div>
  <h3>Rack &amp; Bandwidth</h3>
  <p>Nemo enim ipsam voluptaem, quia voluptas sit, aspernatur aut odit aut fugit, sed quia consequuntur magni dolores eos.</p>
</div>
<div class="abs card" style="left:565px;top:620px">
  <div class="card-icon" role="img" aria-label="Green block icon with a handshake"></div>
  <h3 style="left:128px;top:14px">Reseller &amp; Referral</h3>
  <p style="left:128px;top:36px">Et harum quidem rerum facilis est et expedita distinctio. Nam libero tempore, cum soluta nobis est eligendi optio.</p>
</div>

<section>
  <div class="abs partners-title">OUR TRUSTED PARTNERS</div>
  <div class="abs rule" style="left:220px;top:790px;width:670px"></div>
  <div class="abs rule" style="left:220px;top:838px;width:670px"></div>
  <svg class="abs" style="left:176px;top:803px" width="20" height="30" viewBox="0 0 20 30"><polygon points="18,0 18,30 2,15" fill="#bbb"/></svg>
  <svg class="abs" style="left:913px;top:803px" width="20" height="30" viewBox="0 0 20 30"><polygon points="2,0 2,30 18,15" fill="#bbb"/></svg>
  <div class="abs partner" style="left:226px;width:64px"></div>
  <div class="abs partner" style="left:306px;width:84px"></div>
  <div class="abs partner" style="left:410px;width:100px"></div>
  <div class="abs partner" style="left:529px;width:90px"></div>
  <div class="abs partner" style="left:636px;width:85px"></div>
  <div class="abs partner" style="left:737px;width:62px"></div>
  <div class="abs partner" style="left:811px;width:70px"></div>
</section>

<section>
  <h2 class="abs section-head" style="left:225px;top:858px">Latest News</h2>
  <div class="abs news-head">Lorem ipsum dolor sit amet, consectetur adipisicing</div>
  <p class="abs body-text" style="left:227px;top:907px;width:260px">Elit, sed do eiusmod tempor incididunt ut labore et dolore magna aliqua. Ut enim ad minim veniam, quis nostrud ...</p>
  <a class="abs more" style="left:227px;top:942px" href="#">read more +</a>

  <h2 class="abs section-head" style="left:633px;top:858px">Testimonial</h2>
  <p class="abs body-text" style="left:635px;top:890px;width:262px">“Elit, sed do eiusmod tempor incididunt ut labore et dolore magna aliqua. Ut enim ad minim veniam, quis nostrud qui dolorem ipsum, quia dolor sit amet, consectetur, adipisci[ng] velit, sed quia non numquam [do] eius modi tempora ”</p>
  <a class="abs more" style="left:635px;top:943px" href="#">more testimonials</a>
</section>

<footer>
  <div class="abs footer"></div>
  <div class="abs brand footer-brand"><span class="brand-mark"></span>NEXO47</div>

  <h3 class="abs foot-head" style="left:360px;top:1038px">Site Navigation</h3>
  <ul class="abs foot-list" style="left:361px;top:1060px">
    <li><a href="#">Home</a></li><li><a href="#">About Us</a></li><li><a href="#">Services</a></li><li><a href="#">Case Studies</a></li><li><a href="#">Products</a></li>
  </ul>
  <ul class="abs foot-list" style="left:440px;top:1060px">
    <li><a href="#">Support</a></li><li><a href="#">Contact us</a></li><li><a href="#">Terms</a></li><li><a href="#">Privacy</a></li>
  </ul>

  <h3 class="abs foot-head" style="left:559px;top:1038px">Get In Touch</h3>
  <div class="abs social"><span></span><span></span><span></span><span></span><span></span></div>

  <h3 class="abs foot-head" style="left:775px;top:1038px">Contact Us</h3>
  <p class="abs address">880 Harlow Lane Suite 12<br>Brookfield, NV 40218</p>
  <div class="abs email">info@nexo47.com</div>
  <div class="abs phone footer-phone">
    <svg width="21" height="21" viewBox="0 0 20 20"><circle cx="10" cy="10" r="9" fill="none" stroke="#fff" stroke-width="1.5"/><path d="M7 5.5c-1 .6-1.3 1.8-.8 3.2.9 2.4 2.6 4.3 4.9 5.4 1.3.6 2.5.3 3.1-.6l-1.8-1.7-1.3.8c-1-.5-2-1.6-2.5-2.7l.9-1.2z" fill="#fff"/></svg>
    0-10-5550147
  </div>

  <div class="abs bottom"></div>
  <div class="abs copy">© Copyright 2014 NEXO47 Consulting. All Rights Reserved.</div>
  <div class="abs legal"><a href="#">Terms of Service</a> &nbsp;|&nbsp; <a href="#">Privacy Policy</a> &nbsp;|&nbsp; <a href="#">Contact Us</a></div>
</footer>
</body>
</html>
```